SINGLE PAGE WEBSITE needed for Haunted-House Style Horror Event!

PROJECT:
Single page website to advertise "Midnight Fever"

ABOUT MIDNIGHT FEVER:
Midnight Fever is a Horror Experience event, that will be held on June 1st 2019 at The Lantern Hall in Sydney.

At the event, patrons will enter 6 different rooms and have a horror experience in each one.

There's a bar on-site for them to drink as well.

NEEDS FOR THE WEBSITE:
1. Video banner at top, and scrolling photos after video finishes, and text over the top of the video with the name and date of the event
eg.
"A Night of Immersive Horror Experiences"
"The Lantern Hall | June 1st, 2019"

2. Multiple Book Now buttons on the page, which will link to an external booking platform

3. It should say somewhere "Produced by [BRIGHT HOLLOW PRODUCTIONS LOGO]"

4. A "Next Steps" section that has the steps for them to complete, such as
- Purchase your ticket HERE for one of our waves
- Rock up at the Lantern Hall on June 1st at your wave time
- Experience each of our 6 Interactive Horror Rooms
- Grab some drinks at the bar, a bite to eat, and enjoy a fantastic night out!

Other things that should be included somewhere:
- Testimonials
- FAQs (maybe as a dropdown, so it doesn't take up much space?)
- Contact Form on Footer

- - - -

Images, logos, and more attached!

• 1. Video banner at top, and scrolling photos after video finishes, and text over the top of the video with the name and date of the event
• eg.
• "A Night of Immersive Horror Experiences"
• "The Lantern Hall | June 1st, 2019"
• 2. multiple Book Now buttons on the page, which will link to an external booking platform
• 3. It should say somewhere "Produced by [Bright Hollow Productions LOGO]" with the Bright Hollow logo
• 4. A "Next Steps" section that has the steps for them to complete, such as
• - Purchase your ticket HERE for one of our waves
• - Rock up at the Lantern Hall on June 1st at your wave time
• - Experience each of our 6 Interactive Horror Rooms
• - Grab some drinks at the bar, a bite to eat, and enjoy a fantastic night out!
• Other things that should be included somewhere:
• - Testimonials
• - FAQs (maybe as a dropdown, so it doesn't take up much space?)
• - Contact Form on Footer

```html
<!DOCTYPE html>
<html lang="en">
<head>
<meta charset="utf-8">
<title>Midnight Fever</title>
<link href="https://fonts.googleapis.com/css2?family=Alfa+Slab+One&family=Barlow:ital,wght@0,400;0,500;0,600;0,700;1,600&display=swap" rel="stylesheet">
<style>
:root{
  --green:#9ccb3b;
  --green-dark:#86b22c;
  --ink:#231f20;
  --ink-soft:#2d2a2b;
  --paper:#f3f3f3;
  --mist:#e4e4e4;
  --white:#ffffff;
  --grey:#6d6d6d;
}
*{margin:0;padding:0;box-sizing:border-box}
html,body{width:1200px;height:3416px;overflow:hidden}
body{position:relative;background:var(--white);font-family:"Barlow",sans-serif;color:var(--ink)}
.abs{position:absolute}
.hero-photo{left:0;top:0;width:1200px;height:1000px;background:radial-gradient(ellipse at 30% 35%,#5a3a34 0%,#2b1c1a 40%,#0f0c0c 75%),#111}
.waves{left:0;top:0;width:1200px;height:3416px}
.skull-field{left:0;top:2240px;width:1200px;height:900px;background:linear-gradient(#e9e9e9,#d9d9d9)}
/* header */
.brand{left:132px;top:27px;height:64px;display:flex;align-items:center;gap:12px;font-weight:700;font-size:30px;color:var(--green);text-transform:uppercase;letter-spacing:.5px}
.brand-mark{width:34px;height:34px;border-radius:50%;background:var(--green)}
.nav{left:458px;top:50px;display:flex;gap:30px;font-size:13px;font-weight:600;color:var(--white);letter-spacing:.4px}
.nav .active{color:var(--green)}
.call{left:902px;top:36px;color:var(--white);font-weight:600;font-size:19px}
.call span{color:var(--green);font-weight:500}
.call-email{left:922px;top:63px;color:var(--white);font-size:13px}
/* hero */
.hero-date{left:0;width:1200px;top:288px;text-align:center;color:var(--green);font-size:17px;font-weight:500}
.hero-date sup{font-size:10px}
.hero-title{left:0;width:1200px;top:318px;text-align:center;color:var(--white);font-family:"Alfa Slab One",serif;font-weight:400;line-height:1}
.hero-title .l1{display:block;font-size:52px}
.hero-title .l2{display:block;font-size:40px;margin-top:10px}
.btn{display:flex;align-items:center;justify-content:center;border-radius:20px;font-weight:600;text-transform:uppercase}
.btn-solid{left:521px;top:478px;width:153px;height:37px;background:var(--green);color:var(--white);font-size:15px}
.produced{left:0;width:1200px;top:580px;text-align:center;color:var(--white);font-size:12px;font-weight:600}
.producer-card{left:483px;top:690px;width:237px;height:123px;background:var(--white);border-radius:8px;box-shadow:0 6px 20px rgba(0,0,0,.18);display:flex;align-items:center;justify-content:center;gap:10px}
.producer-card .dot{width:30px;height:30px;background:var(--ink-soft)}
.producer-card b{font-size:16px;font-weight:700;color:var(--ink-soft);line-height:1.1;letter-spacing:1px}
/* steps */
.ticket-icon{left:278px;top:849px;width:95px;height:126px}
.step-text{left:440px;top:896px;font-size:34px;line-height:1.2;color:var(--ink-soft);font-weight:400}
.step-text em{color:var(--green);font-weight:600}
.runner{left:70px;top:1000px;width:240px;height:218px;background:var(--ink);border-radius:40% 60% 30% 50%}
/* cards */
.card{width:280px;height:358px;display:flex;flex-direction:column;justify-content:flex-end;padding:0 28px 30px;color:var(--white)}
.card-1{left:139px;top:1400px;background:linear-gradient(180deg,rgba(0,0,0,0) 40%,rgba(0,0,0,.75)),linear-gradient(160deg,#3d4c63,#7a2a22 55%,#1c1a1b)}
.card-2{left:460px;top:1300px;background:linear-gradient(180deg,rgba(0,0,0,0) 40%,rgba(0,0,0,.8)),linear-gradient(160deg,#6a4a2a,#3b2a1c 55%,#141110)}
.card-3{left:781px;top:1200px;background:linear-gradient(180deg,rgba(0,0,0,0) 40%,rgba(0,0,0,.8)),linear-gradient(160deg,#a9741f,#4a2c14 55%,#151010)}
.card h3{font-family:"Alfa Slab One",serif;font-weight:400;color:var(--green);font-size:34px;line-height:.95}
.card h3 small{display:block;font-size:24px}
.card p{font-size:16px;line-height:1.45;margin-top:12px}
.card .btn-outline{margin-top:16px;width:120px;height:32px;border:2px solid var(--green);color:var(--white);font-size:12px}
/* testimonial */
.quote-mark{left:0;width:1200px;top:2015px;text-align:center;font-family:"Alfa Slab One",serif;font-size:58px;color:var(--ink-soft);line-height:1}
.quote{left:320px;width:560px;top:2077px;text-align:center;font-size:16px;line-height:1.4;color:var(--ink-soft)}
.avatar{left:568px;top:2215px;width:64px;height:64px;border-radius:50%;background:radial-gradient(circle,#6b4a44,#2a1e1c);border:3px solid var(--ink-soft)}
.arrow{top:2238px;width:20px;height:20px;border:1.5px solid var(--ink-soft);border-radius:50%;display:flex;align-items:center;justify-content:center}
.arrow-prev{left:468px}.arrow-next{left:708px}
.person{left:0;width:1200px;top:2293px;text-align:center}
.person b{display:block;font-family:"Alfa Slab One",serif;font-weight:400;font-size:16px}
.person span{font-size:11px;color:var(--ink-soft)}
/* booking */
.book-eyebrow{left:0;width:1200px;top:2644px;text-align:center;color:var(--green);font-size:17px;font-weight:500}
.book-title{left:0;width:1200px;top:2688px;text-align:center;font-family:"Alfa Slab One",serif;font-weight:400;line-height:1}
.book-title .l1{display:block;font-size:36px}
.book-title .l2{display:block;font-size:26px;margin-top:4px}
.field{background:var(--white);border:1px solid #dcdcdc;border-radius:8px;font-size:12px;color:var(--grey);padding:0 22px;display:flex;align-items:center}
.f-name{left:280px;top:2791px;width:223px;height:39px}
.f-email{left:528px;top:2791px;width:223px;height:39px}
.f-phone{left:781px;top:2791px;width:139px;height:39px}
.f-msg{left:280px;top:2855px;width:640px;height:116px;align-items:flex-start;padding-top:14px}
.submit{left:528px;top:3001px;width:144px;height:37px;border:2px solid var(--green);background:var(--white);color:var(--ink);font-size:12px}
/* footer */
.zombie{left:920px;top:3000px;width:250px;height:330px;background:var(--ink);border-radius:45% 40% 0 0}
.foot-col{top:3242px;color:var(--white);font-size:12px;line-height:1.6}
.foot-col h4{color:var(--green);font-size:17px;font-weight:600;margin-bottom:4px}
.fc-1{left:203px}.fc-2{left:519px}.fc-3{left:840px}
.socials{display:flex;gap:10px;margin-top:6px}
.socials i{width:30px;height:30px;border-radius:50%;background:#6b6b6b;display:block}
.copyright{left:203px;top:3346px;color:#bdbdbd;font-size:11px}
.foot-links{left:519px;top:3346px;color:#bdbdbd;font-size:11px}
</style>
</head>
<body>
<div class="abs hero-photo" role="img" aria-label="Dark photo of two horror-costumed performers"></div>
<div class="abs skull-field" role="img" aria-label="Faint grey skull pattern background"></div>

<svg class="abs waves" viewBox="0 0 1200 3416" aria-hidden="true">
  <path d="M0,560 C150,700 260,560 420,600 C600,650 760,560 920,510 C1030,480 1110,440 1200,460 L1200,1100 L0,1100Z" fill="#f3f3f3"/>
  <path d="M0,535 C150,675 270,540 430,575 C610,620 780,540 930,490 C1040,455 1120,410 1200,430" fill="none" stroke="#9ccb3b" stroke-width="2.5"/>
  <path d="M0,1210 C120,1250 200,1140 330,1100 C480,1060 560,1120 700,1070 C850,1010 950,1020 1050,990 C1120,970 1170,960 1200,970 L1200,1900 L0,1900Z" fill="#231f20"/>
  <path d="M0,1850 C150,1880 250,1790 400,1815 C550,1840 620,1765 760,1790 C900,1815 1000,1740 1200,1760 L1200,2400 L0,2400Z" fill="#9ccb3b"/>
  <path d="M0,2280 C150,2290 250,2330 350,2420 C450,2510 600,2520 720,2440 C850,2360 950,2300 1200,2300 L1200,2420 L0,2420Z" fill="#e2e2e2"/>
  <path d="M0,3110 C200,3160 400,3190 600,3170 C800,3150 950,3060 1200,3000 L1200,3416 L0,3416Z" fill="#231f20"/>
</svg>

<header>
  <div class="abs brand"><i class="brand-mark"></i>Midnight Fever</div>
  <nav class="abs nav"><span class="active">ABOUT</span><span>EVENT</span><span>TESTIMONIALS</span><span>FAQ'S</span><span>CONTACT</span></nav>
  <div class="abs call">Call Us. <span>+61 2 9000 4821</span></div>
  <div class="abs call-email">e. info@midnightfever.net</div>
</header>

<section class="hero">
  <p class="abs hero-date">1<sup>st</sup> June 2019, The Lantern Hall</p>
  <h1 class="abs hero-title"><span class="l1">A Night of Immersive</span><span class="l2">Horror Experiences</span></h1>
  <a class="abs btn btn-solid">Book Now!</a>
  <p class="abs produced">Produced By:<br><svg width="12" height="8" viewBox="0 0 12 8"><path d="M1 1l5 5 5-5" fill="none" stroke="#fff" stroke-width="1.5"/></svg></p>
  <div class="abs producer-card"><i class="dot"></i><b>BRIGHT HOLLOW<br>PRODUCTIONS</b></div>
</section>

<section class="steps">
  <svg class="abs ticket-icon" viewBox="0 0 95 126" aria-hidden="true">
    <rect x="6" y="52" width="83" height="52" rx="4" fill="none" stroke="#9ccb3b" stroke-width="5"/>
    <path d="M20 52 L60 14 L80 34" fill="none" stroke="#9ccb3b" stroke-width="5"/>
    <rect x="24" y="68" width="47" height="20" rx="2" fill="none" stroke="#231f20" stroke-width="3"/>
    <path d="M32 78h31" stroke="#231f20" stroke-width="3" stroke-dasharray="4 4"/>
  </svg>
  <p class="abs step-text">Purchase your <em>ticket here</em> for<br>one of our waves</p>
  <div class="abs runner" role="img" aria-label="Silhouette of a running figure"></div>
  <article class="abs card card-1" role="img" aria-label="Photo of a horror character at the theatre">
    <h3>Lantern<small>Hall</small></h3>
    <p>Rock up 1<sup>st</sup> June on your wave time</p>
    <a class="btn btn-outline">Book Now!</a>
  </article>
  <article class="abs card card-2" role="img" aria-label="Photo of a derelict horror room">
    <h3>Horror<small>Rooms</small></h3>
    <p>Experience our 6 interactive horror rooms</p>
  </article>
  <article class="abs card card-3" role="img" aria-label="Photo of a beer and snacks at the bar">
    <h3>Food &amp;<small>Drink</small></h3>
    <p>Grab some drinks at the bar, a bite to eat and enjoy</p>
  </article>
</section>

<section class="testimonial">
  <div class="abs quote-mark">“</div>
  <p class="abs quote">Sed ut perspiciatis unde omnis iste natus error sit voluptatem accusantium doloremque laudantium, totam rem aperiam, eaque ipsa quae ab illo inventore veritatis et quasi architecto beatae vitae dicta sunt explicabo. Nemo enim ipsam voluptatem quia voluptas sit aspernatur aut ...</p>
  <span class="abs arrow arrow-prev"><svg width="8" height="8" viewBox="0 0 8 8"><path d="M5 1L2 4l3 3" fill="none" stroke="#231f20" stroke-width="1.4"/></svg></span>
  <div class="abs avatar" role="img" aria-label="Reviewer portrait"></div>
  <span class="abs arrow arrow-next"><svg width="8" height="8" viewBox="0 0 8 8"><path d="M3 1l3 3-3 3" fill="none" stroke="#231f20" stroke-width="1.4"/></svg></span>
  <div class="abs person"><b>Lorem Ipsum</b><span>Dolor Sit Amet</span></div>
</section>

<section class="booking">
  <p class="abs book-eyebrow">Book your ticket</p>
  <h2 class="abs book-title"><span class="l1">Request A Booking</span><span class="l2">or Quote Now!</span></h2>
  <div class="abs field f-name">Your Name</div>
  <div class="abs field f-email">Email</div>
  <div class="abs field f-phone">Phone</div>
  <div class="abs field f-msg">Message ...</div>
  <a class="abs btn submit">Submit</a>
</section>

<footer>
  <div class="abs zombie" role="img" aria-label="Silhouette of a shambling zombie"></div>
  <div class="abs foot-col fc-1"><h4>Contact Info</h4>Call Us Today. +61 2 9000 4821<br>e. info@midnightfever.net</div>
  <div class="abs foot-col fc-2"><h4>Midnight Fever</h4>48 Ember Lane, Newtown<br>NSW 2042, Australia</div>
  <div class="abs foot-col fc-3"><h4>Our Social</h4><div class="socials"><i></i><i></i><i></i><i></i></div></div>
  <p class="abs copyright">© 2019 Midnight Fever.</p>
  <p class="abs foot-links">About &nbsp;|&nbsp; FAQ's &nbsp;|&nbsp; Contact</p>
</footer>
</body>
</html>
```